Quartz Meridian Business Card Design

I need a 2-sided business card for my computer engineering consulting company. The card is expected to convey a message of cutting edge forward thinking, and boldnes. I would like the card to be memorable and stand-out on a desk. The card should be bold, modern, clean, and highly professional. I am a big fan of watermarks/shadows and other intersting but restrained uses of the logo. The card can be a shape other than the traditional rectangle. Perhaps a rectangle with rounded edges. All I ask is the card be able to fit into a standard wallet. I will supply two logos, one with a red background, and one with a black background. Please feel free to work with both of these logos.
Updates

Hi all, thank you for your submissions. I will post the original vector file later today. Thank you for your patience.

Regards,

Henry

Target Market(s)

Engineering Buyers, Vice Presidents and Directors

Industry/Entity Type

Computer

Requirements
Must have
• 2 sides

```html
<!DOCTYPE html>
<html lang="en">
<head>
<meta charset="utf-8">
<title>Quartz Meridian – Business Card</title>
<link rel="stylesheet" href="https://fonts.googleapis.com/css2?family=Open+Sans:wght@400;600;700&display=swap">
<style>
  :root {
    --stage: #d4d4d4;
    --stage-light: #e6e6e6;
    --card-black: #0b0b0c;
    --card-white: #ffffff;
    --brand-red: #c0202a;
    --brand-red-dark: #a3161f;
    --ink: #2b2b2b;
    --ink-light: #f2f2f2;
    --ink-soft: #8a8a8a;
    --band-grey: #3a3a3c;
  }
  * { box-sizing: border-box; margin: 0; padding: 0; }
  html, body {
    width: 1200px; height: 800px; overflow: hidden;
    background: var(--stage);
    font-family: "Open Sans", Arial, sans-serif;
  }
  .canvas {
    position: relative; width: 1200px; height: 800px;
    background: radial-gradient(circle at 60% 40%, var(--stage-light), var(--stage));
  }
  .card {
    position: absolute; width: 540px; height: 308px;
    border-radius: 26px; overflow: hidden;
    box-shadow: 0 10px 26px rgba(0,0,0,.25);
  }

  /* Shared wordmark */
  .wordmark { display: flex; align-items: center; gap: 12px; }
  .wordmark__mark { flex: none; background: var(--brand-red); }
  .wordmark__name { font-weight: 600; white-space: nowrap; }
  .tagline { color: var(--ink-soft); text-transform: uppercase; white-space: nowrap; }

  /* Front side */
  .card--front { left: 80px; top: 90px; background: var(--card-black); }
  .front-lockup {
    position: absolute; left: 0; right: 0; top: 118px;
    display: flex; flex-direction: column; align-items: center;
  }
  .card--front .wordmark__mark { width: 26px; height: 26px; }
  .card--front .wordmark__name { font-size: 32px; color: var(--ink-light); letter-spacing: .5px; }
  .card--front .tagline { margin-top: 8px; font-size: 12px; letter-spacing: 4px; }

  /* Back side */
  .card--back { left: 580px; top: 400px; background: var(--card-white); }
  .back-band { position: absolute; left: 0; bottom: 0; width: 540px; height: 308px; }
  .back-lockup { position: absolute; left: 28px; top: 30px; }
  .card--back .wordmark__mark { width: 22px; height: 22px; }
  .card--back .wordmark__name { font-size: 23px; color: var(--ink); }
  .card--back .tagline { margin-top: 2px; margin-left: 34px; font-size: 9.5px; letter-spacing: 3px; }

  .person { position: absolute; right: 30px; top: 98px; text-align: right; }
  .person__name { font-weight: 600; font-size: 19px; color: var(--brand-red); }
  .person__role { font-size: 12px; color: var(--ink); }

  .address { position: absolute; left: 48px; top: 140px; font-size: 12px; line-height: 16px; color: var(--ink); }
  .contacts { position: absolute; left: 28px; top: 182px; list-style: none; font-size: 11.5px; color: var(--ink); }
  .contacts li { display: flex; align-items: center; height: 16px; }
  .contacts svg { width: 12px; height: 12px; margin-right: 8px; fill: var(--brand-red); }
</style>
</head>
<body>
<main class="canvas">

  <section class="card card--front" aria-label="Card front">
    <div class="front-lockup">
      <div class="wordmark">
        <span class="wordmark__mark"></span>
        <span class="wordmark__name">Quartz Meridian</span>
      </div>
      <p class="tagline">Engineering The Next Step</p>
    </div>
  </section>

  <section class="card card--back" aria-label="Card back">
    <svg class="back-band" viewBox="0 0 540 308" aria-hidden="true">
      <path d="M0 262 L290 262 C318 262 322 232 352 228 L540 200 L540 308 L0 308 Z" fill="var(--band-grey)"/>
      <path d="M0 276 L296 276 C326 276 326 244 356 238 L540 208 L540 308 L0 308 Z" fill="var(--brand-red)"/>
      <path d="M0 298 L540 298 L540 308 L0 308 Z" fill="var(--brand-red-dark)"/>
    </svg>

    <div class="back-lockup">
      <div class="wordmark">
        <span class="wordmark__mark"></span>
        <span class="wordmark__name">Quartz Meridian</span>
      </div>
      <p class="tagline">Engineering The Next Step</p>
    </div>

    <div class="person">
      <p class="person__name">Marcus Ellery</p>
      <p class="person__role">Managing Director</p>
    </div>

    <p class="address">123 Somewhere Street Name<br>City Name, CN 12345</p>

    <ul class="contacts">
      <li><svg viewBox="0 0 12 12"><path d="M1 4c0-2 2-3 5-3s5 1 5 3l-2 1-1-1H4L3 5zM3 6h6l1 5H2z"/></svg>+0 000 000 0000</li>
      <li><svg viewBox="0 0 12 12"><path d="M3 1h6v3H3zM1 5h10v5H9v1H3v-1H1zm3 3v2h4V8z"/></svg>+0 000 000 0000</li>
      <li><svg viewBox="0 0 12 12"><path d="M4 0h4a1 1 0 0 1 1 1v10a1 1 0 0 1-1 1H4a1 1 0 0 1-1-1V1a1 1 0 0 1 1-1zm0 2v6h4V2z"/></svg>+0 000 000 0000</li>
      <li><svg viewBox="0 0 12 12"><path d="M0 2h12v8H0zm1 1l5 4 5-4z"/></svg>marcus@quartzmeridian.com</li>
      <li><svg viewBox="0 0 12 12"><path d="M6 0a6 6 0 1 0 0 12A6 6 0 0 0 6 0zm0 1.2c.8.8 1.3 2.4 1.4 4.2H4.6C4.7 3.6 5.2 2 6 1.2zM1.2 6.6h2.3c.1 1.6.5 3 1.1 3.9A4.8 4.8 0 0 1 1.2 6.6zm0-1.2a4.8 4.8 0 0 1 3.4-3.9C4 2.4 3.6 3.8 3.5 5.4zm4.8 5.4c-.8-.8-1.3-2.4-1.4-4.2h2.8C7.3 8.4 6.8 10 6 10.8zm1.4-.3c.6-.9 1-2.3 1.1-3.9h2.3a4.8 4.8 0 0 1-3.4 3.9zm1.1-5.1c-.1-1.6-.5-3-1.1-3.9a4.8 4.8 0 0 1 3.4 3.9z"/></svg>www.quartzmeridian.com</li>
    </ul>
  </section>

</main>
</body>
</html>
```